NOTE: I PROVIDED THE INCORRECT LOGO AND ONLY A HANDFUL OF PEOPLE NOTICED THAT IT WAS NOT THE ONE I DESCRIBED. THE LOGO I HAVE NOW ATTACHED MATCHES MY WEBSITE AND THE COLORS ON THE WEBSITE SHOULD BE USED FOR THE CARD.

PLEASE READ THE BUSINESS CARD DETAILS AND PROJECT MUST HAVES CAREFULLY.

I am looking for a business card that is powerful, a bit edgy, and although I work in the corporate world, not too formal. I would like to see designs that use the colors on my website www.brightmoorlane.com. I don't want the card to look washed out so please use shades of those colors that make them "pop". The "vibe" of the card needs to show substance and confidence while also reflecting that we're not your usual consultants.

The focus of my work is turning "people problems" into profits. Those problems could be poor service, an unstable workforce, untrained leaders, or managing change. We are an aggressive, results-focused team of performance improvement professionals who refuse to believe "things can't be done". For us, failure is not an option. Our logo reflects a target from the view of the site on a gun.

In addition to the contact information provided on the sample business card (do not include "turning people problems into profits"), I would like to include this statement (probably on the back):
I equip results-oriented business leaders to turn their people problems into profits in six months or less.

PLEASE NOTE THAT MY WEBSITE IS UNDER REVISION TO TONE DOWN THE MILITARY THEME, ALTHOUGH THE WARRIOR ENERGY AND FOCUS ON RESULTS REMAINS.

Target Market(s)

My clients are Mid and senior-level managers. I don't target any particular industry.

Industry/Entity Type

Consulting

Contact Information for Business Card

In addition to the contact information provided on the sample business card (DO NOT INCLUDE "turning people problems into profits"), I would like to include this statement (probably on the back):

I don't care whether the card is landscape or portrait view.

Font styles to use
Sans Serif

Requirements
Must have
• 1. be easy to read, no 6-8 point fonts!
• 2. a "vibe" that captures the eye without being too chaotic or busy
• 3. bold color, not washed out or boring - a good blend with the colors currently on my website (black, red, white, army green) but you don't need to use all of them.
• 4. all the contact information I have provided
• 5. a good blend with the colors currently on my website
• 6. Must have this quote on the back of the card: I equip results-oriented business leaders to turn their people problems into profits in six months or less.
Nice to have
• In looking at the sample images I provided for ideas, you can see that I like the way a card carries over from one side to the next.
• It would be great to find some aspect/quality/feature that I haven't seen before
Should not have
• 1. NO use of ALL CAPS
• 2. fonts that I would have to seek out and purchase (you should provide files for font if using something not standard)

```html
<!DOCTYPE html>
<html lang="en">
<head>
<meta charset="utf-8">
<title>Brightmoor Lane – Business Card</title>
<link href="https://fonts.googleapis.com/css2?family=Jost:wght@400;500;600&display=swap" rel="stylesheet">
<style>
  :root {
    --bg: #e4e5e7;
    --card-blue: #356591;
    --card-white: #ffffff;
    --accent-green: #8cc63f;
    --brand-green: #7dbb2e;
    --text-light: #ffffff;
    --text-soft: #d9e3ee;
  }
  * { margin: 0; padding: 0; box-sizing: border-box; }
  html, body {
    width: 1200px; height: 1200px; overflow: hidden;
    background: var(--bg);
    font-family: "Jost", "Futura", sans-serif;
  }
  .stage {
    width: 1200px; height: 1200px;
    display: flex; flex-direction: column; align-items: center; justify-content: center;
    gap: 48px;
  }
  .card {
    position: relative;
    width: 700px; height: 400px;
    background: var(--card-blue);
    overflow: hidden;
    box-shadow: 0 6px 18px rgba(0,0,0,0.12);
  }

  /* Back side */
  .card-back .statement {
    position: absolute; left: 110px; right: 60px; top: 40px;
    color: var(--text-light);
    font-weight: 400;
  }
  .statement .lead {
    display: block;
    font-size: 24px; letter-spacing: 1.5px; line-height: 1.3;
  }
  .statement .punch {
    display: block; margin-top: 4px;
    font-size: 64px; letter-spacing: 4px; line-height: 1;
  }
  .statement .tail {
    display: block; margin-top: 6px;
    font-size: 24px; letter-spacing: 1.5px; line-height: 1.3;
  }
  .card-back .stripe {
    position: absolute; left: 0; right: 0; top: 262px; height: 8px;
    background: var(--accent-green);
  }

  /* Front side */
  .card-front .top-panel {
    position: absolute; left: 0; right: 0; top: 0; height: 150px;
    background: var(--card-white);
  }
  .card-front .stripe {
    position: absolute; left: 0; right: 0; top: 150px; height: 8px;
    background: var(--accent-green);
  }
  .brand {
    position: absolute; left: 0; right: 0; top: 52px;
    display: flex; align-items: center; justify-content: center; gap: 14px;
  }
  .brand-mark {
    width: 26px; height: 26px; background: var(--card-blue);
  }
  .brand-name {
    color: var(--brand-green);
    font-size: 44px; font-weight: 500; letter-spacing: 1px;
  }
  .person {
    position: absolute; left: 0; right: 0; top: 170px;
    text-align: center; color: var(--text-light);
  }
  .person .name { font-size: 30px; font-weight: 400; letter-spacing: 1.5px; line-height: 1.2; }
  .person .role { font-size: 20px; color: var(--text-soft); letter-spacing: 1px; line-height: 1.3; margin-top: 2px; }
  .contact {
    position: absolute; color: var(--text-light);
    font-size: 21px; letter-spacing: 1.5px; line-height: 1.55;
  }
  .contact .label { display: inline-block; width: 30px; font-weight: 600; }
  .contact-phone { left: 40px; top: 250px; }
  .contact-web { right: 40px; top: 318px; }
</style>
</head>
<body>
<main class="stage">
  <section class="card card-back" aria-label="Card back">
    <p class="statement">
      <span class="lead">I equip results-oriented business leaders<br>to turn their people problems into</span>
      <span class="punch">Profits</span>
      <span class="tail">in six months or less.</span>
    </p>
    <div class="stripe"></div>
  </section>

  <section class="card card-front" aria-label="Card front">
    <div class="top-panel"></div>
    <div class="stripe"></div>
    <div class="brand">
      <span class="brand-mark"></span>
      <span class="brand-name">Brightmoor Lane Inc</span>
    </div>
    <div class="person">
      <p class="name">Dana Whitfield</p>
      <p class="role">Chief Performance Strategist</p>
    </div>
    <div class="contact contact-phone">
      <p><span class="label">T</span>248 555 0142</p>
      <p><span class="label">M</span>248 555 0187</p>
    </div>
    <div class="contact contact-web">
      <p><span class="label">E</span>dana@brightmoorlane.com</p>
      <p><span class="label">W</span>www.brightmoorlane.com</p>
    </div>
  </section>
</main>
</body>
</html>
```